Brookhollow dog Kennel -Loyalty Card

We are a bod boarding and training Kennel located in Egypt and we would like to design a member loyalty card. The card need to be fun, funky. I would like the logo to appear on the card. On the back side we will list the benefits and on the bottom side of the card will will have the logos of our partner companies

Target Market(s)

clientele from dog lovers. Age 25 and above. 65% women.

Industry/Entity Type

Training

Font styles to use
Sans Serif

Colors
0555a3
33a6d7
0792cd

Requirements
Must have
• Brookhollow Logo and bleu colours.
Nice to have
• a dog figure
Should not have
• dark serious colours or aggressive looking dogs or dog breeds

```html
<!DOCTYPE html>
<html lang="en">
<head>
<meta charset="utf-8">
<title>Brookhollow dog Kennel – Loyalty Card</title>
<link href="https://fonts.googleapis.com/css2?family=Comfortaa:wght@400;700&display=swap" rel="stylesheet">
<style>
  :root {
    --page: #eef1f4;
    --card-blue: #45c0ee;
    --card-blue-light: #7fd6f5;
    --card-blue-deep: #1ea8e0;
    --brand-navy: #0555a3;
    --brand-mid: #0792cd;
    --brand-sky: #33a6d7;
    --white: #ffffff;
    --dog-gold: #d9a05b;
    --dog-cream: #f0d3a3;
  }
  * { box-sizing: border-box; margin: 0; padding: 0; }
  html, body {
    width: 1200px; height: 1000px; overflow: hidden;
    background: var(--page);
    font-family: "Comfortaa", sans-serif;
  }
  .sheet {
    position: relative; width: 1200px; height: 1000px;
    display: flex; justify-content: center; align-items: center; gap: 80px;
  }
  .card {
    position: relative; width: 380px; height: 620px;
    border-radius: 6px; overflow: hidden;
    box-shadow: 0 14px 30px rgba(0, 40, 80, 0.22);
  }

  /* Benefits side */
  .card--benefits { background: var(--card-blue); }
  .benefits-head {
    height: 112px; background: var(--card-blue-light);
    display: flex; flex-direction: column; justify-content: center; align-items: center; gap: 12px;
  }
  .dotted-rule { width: 330px; border-top: 4px dotted var(--brand-navy); opacity: .8; }
  .benefits-title { font-size: 38px; font-weight: 400; letter-spacing: 3px; color: var(--brand-navy); }
  .benefit-list { list-style: none; padding: 24px 0 0 34px; }
  .benefit-item {
    display: flex; gap: 10px; margin-bottom: 16px;
    color: var(--white); font-size: 19px; line-height: 1.05; font-weight: 700;
  }
  .benefit-item svg { flex: none; margin-top: 2px; }
  .partners-area { position: absolute; left: 0; right: 0; bottom: 0; height: 250px; }
  .dog-photo {
    position: absolute; left: 0; bottom: 28px; width: 200px; height: 210px;
    border-radius: 48% 48% 8px 8px;
    background: radial-gradient(circle at 50% 35%, var(--dog-cream), var(--dog-gold) 75%);
  }
  .partner-grid {
    position: absolute; right: 22px; bottom: 46px;
    display: grid; grid-template-columns: 78px 78px; gap: 10px 16px;
  }
  .partner-badge {
    width: 78px; height: 78px; border-radius: 50%;
    background: var(--white); border: 4px solid var(--brand-sky);
    display: flex; align-items: center; justify-content: center;
  }
  .partner-badge span { width: 34px; height: 34px; border-radius: 50%; background: var(--card-blue-light); }
  .bottom-rule {
    position: absolute; left: 210px; right: 22px; bottom: 20px;
    border-top: 4px dotted var(--brand-navy); opacity: .8;
  }

  /* Brand side */
  .card--brand {
    background: linear-gradient(160deg, var(--card-blue-light) 0%, var(--card-blue) 45%, var(--card-blue-deep) 100%);
  }
  .swirl-field {
    position: absolute; inset: 0;
    background:
      radial-gradient(circle at 30% 18%, rgba(5, 85, 163, .28), transparent 38%),
      radial-gradient(circle at 80% 72%, rgba(255, 255, 255, .35), transparent 34%),
      radial-gradient(circle at 20% 85%, rgba(7, 146, 205, .45), transparent 40%);
  }
  .brand-mark {
    position: absolute; left: 0; right: 0; top: 250px;
    display: flex; align-items: center; justify-content: center; gap: 16px;
  }
  .brand-square { flex: none; width: 64px; height: 64px; background: var(--brand-navy); }
  .brand-name { font-size: 40px; font-weight: 700; color: var(--white); line-height: 1.1; }
</style>
</head>
<body>
<main class="sheet">

  <section class="card card--benefits" aria-label="Loyalty card benefits side">
    <header class="benefits-head">
      <div class="dotted-rule"></div>
      <h2 class="benefits-title">BENEFITS</h2>
      <div class="dotted-rule"></div>
    </header>
    <ul class="benefit-list">
      <li class="benefit-item"><svg width="16" height="16" viewBox="0 0 16 16"><polygon points="4,1 12,1 15,8 12,15 4,15 1,8" fill="none" stroke="#fff" stroke-width="2"/></svg>Lorem Ipsum is simply<br>dummy text</li>
      <li class="benefit-item"><svg width="16" height="16" viewBox="0 0 16 16"><polygon points="4,1 12,1 15,8 12,15 4,15 1,8" fill="none" stroke="#fff" stroke-width="2"/></svg>Lorem Ipsum is simply<br>dummy text</li>
      <li class="benefit-item"><svg width="16" height="16" viewBox="0 0 16 16"><polygon points="4,1 12,1 15,8 12,15 4,15 1,8" fill="none" stroke="#fff" stroke-width="2"/></svg>Lorem Ipsum is simply<br>dummy text</li>
      <li class="benefit-item"><svg width="16" height="16" viewBox="0 0 16 16"><polygon points="4,1 12,1 15,8 12,15 4,15 1,8" fill="none" stroke="#fff" stroke-width="2"/></svg>Lorem Ipsum is simply<br>dummy text</li>
    </ul>
    <div class="partners-area">
      <div class="dog-photo" role="img" aria-label="Photo of a friendly golden retriever lying down"></div>
      <div class="partner-grid" aria-label="Partner companies">
        <div class="partner-badge"><span></span></div>
        <div class="partner-badge"><span></span></div>
        <div class="partner-badge"><span></span></div>
        <div class="partner-badge"><span></span></div>
      </div>
      <div class="bottom-rule"></div>
    </div>
  </section>

  <section class="card card--brand" aria-label="Loyalty card brand side">
    <div class="swirl-field" role="img" aria-label="Playful blue background of swirling lines, soft circles and faint training figures"></div>
    <div class="brand-mark">
      <div class="brand-square"></div>
      <div class="brand-name">Brookhollow<br>Training</div>
    </div>
  </section>

</main>
</body>
</html>
```